Medical VIP club - small design

Please read the specs in a design brief attached. Also we don't have logo in a Vector format and attaching the only version we have.

Industry/Entity Type

Club

```html
<!DOCTYPE html>
<html lang="en">
<head>
<meta charset="utf-8">
<title>Veridana — VIP Club</title>
<link rel="stylesheet" href="https://fonts.googleapis.com/css2?family=Roboto+Condensed:wght@300;400;700&family=Lustria&display=swap">
<style>
  :root {
    --bg-dark: #5b4a37;
    --bg-light: #a39680;
    --cream: #fbf9ec;
    --cream-shade: #e6e0c6;
    --nav-text: #4a3b2a;
    --accent: #8c2a10;
    --dropdown: rgba(176, 156, 128, 0.8);
    --white: #ffffff;
    --ivory: #f5efd6;
    --gold: #e3c98f;
    --bronze: #8a6536;
    --umber: #3a2716;
  }
  * { box-sizing: border-box; margin: 0; padding: 0; }
  html, body { width: 1200px; height: 900px; overflow: hidden; }
  body {
    position: relative;
    font-family: "Roboto Condensed", "Arial Narrow", sans-serif;
    background: linear-gradient(180deg, var(--bg-dark) 0%, #6d5d48 38%, var(--bg-light) 56%, #6d5d48 72%, var(--bg-dark) 100%);
  }
  .brand {
    position: absolute; left: 150px; top: 36px; width: 320px; height: 104px;
    display: flex; align-items: center; gap: 14px; padding-left: 6px;
    background: radial-gradient(ellipse at center, rgba(250,245,225,.38) 0%, rgba(250,245,225,0) 70%);
  }
  .brand-mark { width: 30px; height: 30px; border-radius: 50%; background: var(--cream-shade); }
  .brand-name { font-family: "Lustria", Georgia, serif; font-size: 50px; color: var(--ivory); }

  .site-frame {
    position: absolute; left: 127px; top: 137px; width: 946px; height: 704px;
    border-radius: 24px; overflow: hidden;
    background: linear-gradient(180deg, #ede8d1 0%, var(--cream) 35%, #f3efdc 70%, #d9d2b5 100%);
    box-shadow: 0 4px 14px rgba(0,0,0,.35);
  }
  .main-nav { display: flex; height: 74px; }
  .main-nav a {
    flex: 1; display: flex; align-items: flex-end; justify-content: center; padding-bottom: 14px;
    font-size: 19px; font-weight: 300; color: var(--nav-text); text-decoration: none; letter-spacing: -0.2px;
    border-left: 1px solid #cfc8ad; border-radius: 22px 0 0 0;
    background: linear-gradient(180deg, #fdfcf4 0%, #f1edd8 100%);
  }
  .main-nav a:first-child { border-left: 0; }
  .main-nav a.nav-register { color: var(--accent); font-weight: 700; }

  .hero {
    position: absolute; left: 0; top: 74px; width: 946px; height: 422px;
    background:
      radial-gradient(ellipse 18% 40% at 47% 22%, rgba(255,236,190,.85) 0%, rgba(255,236,190,0) 100%),
      radial-gradient(ellipse 14% 30% at 47% 55%, rgba(120,90,55,.9) 0%, rgba(120,90,55,0) 100%),
      linear-gradient(180deg, rgba(0,0,0,0) 60%, rgba(90,62,32,.55) 80%, rgba(60,40,20,.7) 100%),
      radial-gradient(ellipse 22% 35% at 12% 60%, rgba(225,210,180,.55) 0%, rgba(225,210,180,0) 100%),
      radial-gradient(ellipse 22% 35% at 84% 60%, rgba(225,210,180,.5) 0%, rgba(225,210,180,0) 100%),
      radial-gradient(ellipse 10% 25% at 32% 78%, rgba(240,190,100,.55) 0%, rgba(240,190,100,0) 100%),
      radial-gradient(ellipse 10% 25% at 66% 78%, rgba(240,190,100,.55) 0%, rgba(240,190,100,0) 100%),
      linear-gradient(90deg, var(--umber) 0%, #6b4a2a 8%, var(--bronze) 22%, #b8966a 38%, #9c7a4f 50%, #b8966a 62%, var(--bronze) 78%, #6b4a2a 92%, var(--umber) 100%);
  }
  .hero-title {
    position: absolute; left: 523px; top: 28px;
    font-family: "Lustria", Georgia, serif; font-weight: 400; font-size: 94px; color: var(--ivory); line-height: 1;
    text-shadow: 0 2px 5px rgba(0,0,0,.4);
  }
  .hero-lines { position: absolute; left: 623px; top: 130px; font-size: 32px; font-weight: 300; color: var(--white); line-height: 42px; letter-spacing: -0.3px; text-shadow: 0 1px 3px rgba(0,0,0,.35); }
  .hero-arrow { position: absolute; top: 264px; width: 56px; height: 56px; }
  .hero-arrow.prev { left: 13px; }
  .hero-arrow.next { left: 870px; }

  .submenu {
    position: absolute; left: 0; top: 74px; width: 148px; height: 141px;
    background: var(--dropdown); border-radius: 0 0 12px 12px; list-style: none; padding-top: 14px;
  }
  .submenu li { font-size: 16px; font-weight: 300; color: var(--white); padding-left: 41px; height: 42px; }

  .feature-strip { position: absolute; left: 0; top: 496px; width: 946px; height: 131px; display: flex; border-radius: 22px 22px 0 0; overflow: hidden; background: #cbb89a; }
  .feature-tile { height: 100%; border-left: 3px solid #cbb89a; border-radius: 20px 0 0 0; }
  .feature-tile:first-child { border-left: 0; }
  .tile-signs { width: 180px; background:
      linear-gradient(180deg, rgba(0,0,0,0) 20%, rgba(200,30,40,.85) 22%, rgba(200,30,40,.85) 30%, rgba(0,0,0,0) 32%),
      linear-gradient(150deg, #4a4a50 0%, #26262b 55%, #111114 100%); }
  .tile-staff { width: 173px; background:
      radial-gradient(ellipse 70% 45% at 55% 85%, rgba(235,240,246,.95) 0%, rgba(235,240,246,0) 100%),
      linear-gradient(180deg, #e2ecf5 0%, #a9bfd6 55%, #6f8fb3 100%); }
  .tile-spa { width: 188px; background:
      radial-gradient(ellipse 35% 40% at 70% 40%, rgba(225,205,170,.8) 0%, rgba(225,205,170,0) 100%),
      linear-gradient(180deg, #d2e2df 0%, #8fb0ab 55%, #4f6e6a 100%); }
  .tile-flight { width: 193px; background:
      radial-gradient(ellipse 40% 25% at 50% 50%, rgba(235,240,248,.7) 0%, rgba(235,240,248,0) 100%),
      linear-gradient(180deg, #1f4e98 0%, #3f74bd 45%, #a9c6e6 100%); }
  .tile-view { width: 212px; background:
      linear-gradient(180deg, rgba(0,0,0,0) 62%, rgba(40,40,40,.55) 64%, rgba(60,80,50,.6) 100%),
      radial-gradient(ellipse 25% 50% at 48% 60%, rgba(210,180,120,.8) 0%, rgba(210,180,120,0) 100%),
      linear-gradient(180deg, #c3d4e6 0%, #9fb7cd 45%, #7b9a68 100%); }

  .site-footer { position: absolute; left: 0; top: 627px; width: 946px; height: 77px; display: flex; align-items: center; gap: 12px; padding-left: 329px; }
  .follow-label { font-size: 13px; color: var(--nav-text); margin-right: 6px; letter-spacing: -0.2px; }
  .social-link { display: flex; align-items: center; gap: 6px; font-size: 13px; color: var(--nav-text); text-decoration: none; }
  .social-link::before { content: ""; width: 36px; height: 36px; border-radius: 6px; }
  .social-chirper::before { background: #7cc3e0; }
  .social-feed::before { background: #e06a2a; }
  .social-friendbook::before { background: #3b5b9a; }

  .bottom-links { position: absolute; left: 0; top: 851px; width: 1200px; text-align: center; font-size: 15px; font-weight: 300; color: var(--white); }
  .bottom-links a { color: var(--white); text-decoration: none; }
  .bottom-links span { margin: 0 12px; }
</style>
</head>
<body>
  <div class="brand">
    <span class="brand-mark"></span>
    <span class="brand-name">Veridana</span>
  </div>

  <div class="site-frame">
    <nav class="main-nav">
      <a href="#">About us</a>
      <a href="#">VIP Club</a>
      <a href="#">Services</a>
      <a href="#">Packages @ Prices</a>
      <a href="#">Contacs</a>
      <a href="#" class="nav-register">Registration</a>
    </nav>

    <section class="hero" role="img" aria-label="Luxurious golden hall with chandeliers, tall vases and glowing lanterns">
      <h1 class="hero-title">VIP Club</h1>
      <p class="hero-lines">Lorep Epsum...<br>Lorep Epsum...</p>
      <svg class="hero-arrow prev" viewBox="0 0 56 56" aria-hidden="true">
        <circle cx="28" cy="28" r="25" fill="rgba(0,0,0,.15)" stroke="#fff" stroke-width="4"/>
        <path d="M40 28H17M27 17 16 28l11 11" fill="none" stroke="#fff" stroke-width="5" stroke-linecap="round" stroke-linejoin="round"/>
      </svg>
      <svg class="hero-arrow next" viewBox="0 0 56 56" aria-hidden="true">
        <circle cx="28" cy="28" r="25" fill="rgba(0,0,0,.15)" stroke="#fff" stroke-width="4"/>
        <path d="M16 28h23M29 17l11 11-11 11" fill="none" stroke="#fff" stroke-width="5" stroke-linecap="round" stroke-linejoin="round"/>
      </svg>
    </section>

    <ul class="submenu">
      <li>success story</li>
      <li>recognition</li>
      <li>specialists</li>
    </ul>

    <div class="feature-strip">
      <div class="feature-tile tile-signs" role="img" aria-label="Hospital direction signs"></div>
      <div class="feature-tile tile-staff" role="img" aria-label="Team of medical staff"></div>
      <div class="feature-tile tile-spa" role="img" aria-label="Relaxing by a window at a resort"></div>
      <div class="feature-tile tile-flight" role="img" aria-label="Airplane in a blue sky"></div>
      <div class="feature-tile tile-view" role="img" aria-label="Couple on a balcony overlooking the landscape"></div>
    </div>

    <footer class="site-footer">
      <span class="follow-label">Follow us on</span>
      <a href="#" class="social-link social-chirper">Chirper</a>
      <a href="#" class="social-link social-feed">Feed</a>
      <a href="#" class="social-link social-friendbook">Friendbook</a>
    </footer>
  </div>

  <nav class="bottom-links">
    <a href="#">Home</a><span>I</span><a href="#">Services</a><span>I</span><a href="#">About us</a><span>I</span><a href="#">Contact us</a>
  </nav>
</body>
</html>
```